Banner ad design for Vantora Display Ads

We are looking for a designer to develop a concept for banner ads for a Vantora Display campaign we are building.

We have 3 business lines, shredding services, records management services and scanning services.

We are looking for 4 sets of ads to be created, one for each business line + one set that showcases all of our lines together.

For the design concepts, we would like to see a few sizes (banner, square, leaderboard, skyscraper, etc) for each.

The person chosen will then need to create the ads into all Vantora supported sizes -- 20 sizes total for each set of ads as per the Vantora size guidelines found on this page - https://help.vantora-example.com/vantora-ads/answer/4827150?hl=en&ref_topic=6604821#

A few items to note:
- Design should complement our existing brand/website look and feel (www.oak-ferry.ca)
- Each final ad must be 150Kb or less in size
- Final designs should be editable, meaning if we would like to change some copy in the design, we can do so using a well-known software (Canva, Photoshop/InDesign, etc)
- Some images are attached for use, but if you feel a different stock image is more suitable to to your design, please go ahead and use it.

Provided below is some messaging that can be used for each set of ads. Do not feel you need to use all of the messaging, it is provided for guidance.

SHREDDING SERVICES:

Possible Short Headline:
-- One-Time Shredding Services
-- Secure Shredding Services
-- Affordable On-Site Shredding

Possible Long Headline
-- Your Paper Can be Destroyed as Soon as the Next Business Day

Possible Descriptions:
-- KVEC Gold Certified On site shredding company. Service as soon as Next Day.
-- Secure and Affordable Toronto & GTA On-Site Shredding.
-- Certified, Affordable Office Shredding Since 2003.
-- Quick, no contact and affordable paper shredding services in Toronto & Southern Ontario.
-- Certified, Affordable Office Shredding Since 2003. Fast, no contact shredding service.

Call to Action
-- Get a Quote

RECORDS MANAGEMENT
Short Headline:
-- Off-site Records Storage
-- Records Management & Storage
-- Secure Records Storage
-- Records Management Services
-- Long Term Records Management
-- Document Storage Solutions

Possible Description
-- Local, Affordable Storage Solutions. Protect and Store your Documents in our Secure Facility
-- Local, Affordable Records Management Solutions. Store your Records in our Secure Facility
-- Certified, Affordable Document Storage Since 2004. Contact Us for a Free Quote!
-- Vaultline+ Certified, Affordable Document Storage Since 2004. Contact Us for a Free Quote!

Call to Action
-- Get a Quote

SCANNING SERVICES

Short Headline:
-- Professional Scanning Company
-- Toronto & GTA Scanning Service
-- Document Scanning Services
-- Digital Conversion Services
-- Fast & Easy Retrieval

Description
-- Scan and documents and files with Professional scanning services from Oak-Ferry
-- Convert Your Paper Files to Electronic Files. Fast & Easy Retrieval.
-- Easily access your documents electronically with Document Scanning Services

Call to Action
-- Get a Quote

ALL SERVICES AD SET
Short Headline
-- Shred, Scan & Store Documents
-- Secure Shredding, Records Management and Scanning Services
-- #1 Document Management Company
-- Oak Ferry Shredding, Storage & Scanning

Description
-- Secure and Affordable Toronto & GTA On-Site Shredding, Document Storage & Scanning Company

Call to Action
-- Get a Quote

Font styles to use
Sans Serif

```html
<!DOCTYPE html>
<html lang="en">
<head>
<meta charset="utf-8">
<title>Oak-Ferry Display Banners</title>
<link href="https://fonts.googleapis.com/css2?family=Source+Sans+3:wght@400;600;700&display=swap" rel="stylesheet">
<style>
  :root{
    --navy:#03143a;
    --brand-blue:#0a9be0;
    --blue-light:#35b3ee;
    --green:#1fc25a;
    --green-deep:#16a94b;
    --white:#ffffff;
    --photo-light:#dfe3e6;
    --photo-mid:#b9bfc4;
    --photo-warm:#d9b64a;
    --photo-dark:#4a5058;
  }
  *{box-sizing:border-box;margin:0;padding:0}
  html,body{width:1200px;height:1200px;overflow:hidden}
  body{background:var(--navy);font-family:"Source Sans 3",Arial,sans-serif;color:var(--white);position:relative}
  .banner{position:absolute;left:120px;overflow:hidden}
  .banner svg{position:absolute;inset:0;display:block}
  .banner--all{top:91px;width:970px;height:249px}
  .banner--records{top:357px;width:962px;height:246px}
  .banner--scanning{top:621px;width:962px;height:247px}
  .banner--shredding{top:886px;width:962px;height:246px}

  .brand{position:absolute;left:27px;top:40px;line-height:1}
  .brand__name{display:block;font-weight:700;font-size:29px;letter-spacing:-.2px}
  .brand__tagline{display:block;font-weight:400;font-size:17px;margin-top:1px}

  .headline{position:absolute;left:26px;font-weight:700;font-size:31px;line-height:34px;letter-spacing:-.2px;white-space:nowrap}
  .description{position:absolute;left:26px;font-weight:400;font-size:22px;line-height:25px}

  .cta{position:absolute;width:127px;height:44px;border-radius:8px;background:var(--green);
       box-shadow:0 2px 5px rgba(0,0,0,.25);display:flex;align-items:center;justify-content:center;
       font-weight:700;font-size:17px;letter-spacing:-.1px}

  .service-label{position:absolute;font-weight:700;font-size:19px;line-height:16px;text-shadow:0 1px 2px rgba(0,0,0,.25)}

  .banner--all .headline{top:128px;font-size:29px}
  .banner--all .description{top:163px;font-size:21px;line-height:24px}
  .banner--all .cta{left:392px;top:37px}

  .banner--records .headline{top:108px}
  .banner--records .description{top:146px}
  .banner--records .cta{left:820px;top:14px}

  .banner--scanning .headline{top:108px}
  .banner--scanning .description{top:148px}
  .banner--scanning .cta{left:819px;top:14px}

  .banner--shredding .brand{top:38px}
  .banner--shredding .headline{top:102px}
  .banner--shredding .description{top:174px;font-size:21px;line-height:24px}
  .banner--shredding .cta{left:818px;top:14px}
</style>
</head>
<body>

<!-- All services -->
<section class="banner banner--all">
  <svg viewBox="0 0 970 249" width="970" height="249">
    <defs>
      <linearGradient id="allPhotoA" x1="0" y1="0" x2="1" y2="1">
        <stop offset="0" stop-color="#e9ecee"/><stop offset="1" stop-color="#b7bcc1"/>
      </linearGradient>
      <linearGradient id="allPhotoB" x1="0" y1="0" x2="0" y2="1">
        <stop offset="0" stop-color="#c9c4bb"/><stop offset=".5" stop-color="var(--photo-warm)"/><stop offset="1" stop-color="#3e434a"/>
      </linearGradient>
      <linearGradient id="allPhotoC" x1="0" y1="0" x2="1" y2="1">
        <stop offset="0" stop-color="#d7d9d4"/><stop offset="1" stop-color="#575c63"/>
      </linearGradient>
      <linearGradient id="greenFade" x1="0" y1="0" x2="0" y2="1">
        <stop offset="0" stop-color="var(--green)" stop-opacity="1"/><stop offset=".55" stop-color="var(--green)" stop-opacity="0"/>
      </linearGradient>
      <linearGradient id="greenFadeUp" x1="0" y1="1" x2="0" y2="0">
        <stop offset="0" stop-color="var(--green)" stop-opacity="1"/><stop offset=".45" stop-color="var(--green)" stop-opacity="0"/>
      </linearGradient>
      <linearGradient id="blueBackdrop" x1="0" y1="0" x2="1" y2="0">
        <stop offset="0" stop-color="var(--blue-light)" stop-opacity="0"/><stop offset=".6" stop-color="var(--blue-light)" stop-opacity=".35"/><stop offset="1" stop-color="var(--blue-light)" stop-opacity="0"/>
      </linearGradient>
    </defs>
    <g role="img" aria-label="Hand feeding paper into a secure shredding console">
      <polygon points="600,0 700,0 790,249 650,249" fill="url(#allPhotoA)"/>
    </g>
    <g role="img" aria-label="Records storage room with stacked files and yellow archive boxes">
      <polygon points="690,0 820,0 900,249 770,249" fill="url(#allPhotoB)"/>
    </g>
    <g role="img" aria-label="Staff member loading documents into a scanner">
      <polygon points="810,0 970,0 970,249 890,249" fill="url(#allPhotoC)"/>
    </g>
    <polygon points="600,0 700,0 760,160 650,249" fill="url(#greenFade)"/>
    <polygon points="820,0 970,0 970,160 880,150" fill="url(#greenFade)"/>
    <polygon points="775,180 860,180 900,249 790,249" fill="url(#greenFadeUp)"/>
    <polygon points="690,0 703,0 790,249 777,249" fill="var(--green)"/>
    <polygon points="815,0 826,0 904,249 893,249" fill="var(--green)"/>
    <polygon points="661,0 680,0 783,249 772,249" fill="var(--green)" opacity=".8"/>
    <polygon points="547,249 600,118 655,249" fill="var(--white)"/>
    <polygon points="0,0 541,0 600,118 547,249 0,249" fill="var(--brand-blue)"/>
    <polygon points="541,0 605,0 660,120 600,118" fill="var(--green)"/>
    <g role="img" aria-label="Faded photo of a uniformed courier handing over a document box">
      <rect x="250" y="0" width="310" height="150" fill="url(#blueBackdrop)"/>
    </g>
  </svg>
  <div class="brand"><span class="brand__name">oak-ferry</span><span class="brand__tagline">Information Security</span></div>
  <a class="cta">GET A QUOTE</a>
  <h1 class="headline">#1 Document Management Company</h1>
  <p class="description">Secure and Affordable Toronto &amp; GTA On-Site Shredding,<br>Document Storage &amp; Scanning Company</p>
  <span class="service-label" style="left:592px;top:20px">Shredding<br>Services</span>
  <span class="service-label" style="left:846px;top:20px">Scanning<br>Services</span>
  <span class="service-label" style="left:793px;top:207px">Records<br>Management</span>
</section>

<!-- Records management -->
<section class="banner banner--records">
  <svg viewBox="0 0 962 246" width="962" height="246">
    <defs>
      <linearGradient id="recPhoto" x1="0" y1="0" x2="0" y2="1">
        <stop offset="0" stop-color="#e3e6e8"/><stop offset=".3" stop-color="#a9a39a"/><stop offset=".55" stop-color="var(--photo-warm)"/><stop offset="1" stop-color="#555a61"/>
      </linearGradient>
      <linearGradient id="recBackdrop" x1="0" y1="0" x2="1" y2="0">
        <stop offset="0" stop-color="var(--blue-light)" stop-opacity="0"/><stop offset=".7" stop-color="var(--blue-light)" stop-opacity=".35"/><stop offset="1" stop-color="var(--blue-light)" stop-opacity=".1"/>
      </linearGradient>
    </defs>
    <rect width="962" height="246" fill="var(--white)"/>
    <g role="img" aria-label="Records storage room with stacked files, archive boxes and a staff member at a desk">
      <polygon points="676,0 962,0 962,246 740,246" fill="url(#recPhoto)"/>
    </g>
    <polygon points="607,0 676,0 643,80" fill="var(--green)"/>
    <polygon points="0,0 603,0 712,246 0,246" fill="var(--brand-blue)"/>
    <g role="img" aria-label="Faded photo of a hand pulling a file folder from a shelf">
      <polygon points="250,0 603,0 660,130 250,130" fill="url(#recBackdrop)"/>
    </g>
  </svg>
  <div class="brand"><span class="brand__name">oak-ferry</span><span class="brand__tagline">Information Security</span></div>
  <a class="cta">GET A QUOTE</a>
  <h2 class="headline">Records Management &amp; Storage</h2>
  <p class="description">Local, Affordable Records Management Solutions. Store your<br>Records in our Secure Facility</p>
</section>

<!-- Scanning -->
<section class="banner banner--scanning">
  <svg viewBox="0 0 962 247" width="962" height="247">
    <defs>
      <linearGradient id="scanPhoto" x1="0" y1="0" x2="1" y2="1">
        <stop offset="0" stop-color="#d8d4cc"/><stop offset=".45" stop-color="#eef0f1"/><stop offset="1" stop-color="#3f444a"/>
      </linearGradient>
      <linearGradient id="scanBackdrop" x1="0" y1="0" x2="1" y2="0">
        <stop offset="0" stop-color="var(--blue-light)" stop-opacity="0"/><stop offset=".6" stop-color="var(--blue-light)" stop-opacity=".35"/><stop offset="1" stop-color="var(--blue-light)" stop-opacity=".1"/>
      </linearGradient>
    </defs>
    <rect width="962" height="247" fill="var(--white)"/>
    <g role="img" aria-label="Staff member feeding a stack of documents into a scanner">
      <polygon points="676,0 962,0 962,247 740,247" fill="url(#scanPhoto)"/>
    </g>
    <polygon points="607,0 676,0 645,92" fill="var(--green)"/>
    <polygon points="0,0 603,0 712,247 0,247" fill="var(--brand-blue)"/>
    <g role="img" aria-label="Faded photo of an office with desks and stacked files">
      <polygon points="230,0 603,0 660,130 230,130" fill="url(#scanBackdrop)"/>
    </g>
  </svg>
  <div class="brand"><span class="brand__name">oak-ferry</span><span class="brand__tagline">Information Security</span></div>
  <a class="cta">GET A QUOTE</a>
  <h2 class="headline">Professional Scanning Company</h2>
  <p class="description">Easily access your documents electronically with Document<br>Scanning Services</p>
</section>

<!-- Shredding -->
<section class="banner banner--shredding">
  <svg viewBox="0 0 962 246" width="962" height="246">
    <defs>
      <linearGradient id="shredPhoto" x1="0" y1="0" x2="1" y2="1">
        <stop offset="0" stop-color="#eef0f1"/><stop offset=".6" stop-color="#dfe4e7"/><stop offset="1" stop-color="#a8c9de"/>
      </linearGradient>
      <linearGradient id="shredBackdrop" x1="0" y1="0" x2="1" y2="0">
        <stop offset="0" stop-color="var(--blue-light)" stop-opacity="0"/><stop offset=".6" stop-color="var(--blue-light)" stop-opacity=".35"/><stop offset="1" stop-color="var(--blue-light)" stop-opacity=".1"/>
      </linearGradient>
    </defs>
    <rect width="962" height="246" fill="var(--white)"/>
    <g role="img" aria-label="Hand placing paper into a locked shredding console with a plant behind">
      <polygon points="676,0 962,0 962,246 740,246" fill="url(#shredPhoto)"/>
    </g>
    <polygon points="607,0 676,0 643,88" fill="var(--green)"/>
    <polygon points="0,0 603,0 712,246 0,246" fill="var(--brand-blue)"/>
    <g role="img" aria-label="Faded photo of an office worker placing paper in a shredding bin">
      <polygon points="230,0 603,0 660,130 230,130" fill="url(#shredBackdrop)"/>
    </g>
  </svg>
  <div class="brand"><span class="brand__name">oak-ferry</span><span class="brand__tagline">Information Security</span></div>
  <a class="cta">GET A QUOTE</a>
  <h2 class="headline">Your Paper Can be Destroyed<br>as Soon as the Next Business Day</h2>
  <p class="description">Quick, no contact and affordable paper shredding services in<br>Toronto &amp; Southern Ontario.</p>
</section>

</body>
</html>
```